WebHaven Sentry (Parental Guidance software) brochure

We want a brochure that gives an overview of the service that we provide which can be emailled to users at their request. Including the front cover it should be 4-5 pages in length. The website https://www.webhavensentry.co.uk describes our service.
The industry terms our app Parental Control but we call it Parental Guidance so we don't want the term Parental Control on here.

We can provide the text that can go into the brochure. The design should be informal but informative. We are also a member of the NCB and DSR so we need to include logos in the brochure somewhere.

Target Market(s)

The target market is parents who are visiting the website, this will be a downloadable brochure.

Industry/Entity Type

Information Technology

Requirements
Must have
• The front of the brochure should be a cover page with images and the words "Parental Guidance with WebHaven Sentry"
• The second page should have some text about the service and a small piece about the company behind it, Marlow IT Ltd and some of the main features of the service i.e. what it can do including some screenshots.
• The third page would have statistics such as
• Page 3
• Statistics page –
• 1 in 3 Internet users are children.
• 1 in 5 eight to eleven-year olds have a social media profile.
• 1 in 3 children have been a victim of cyberbullying.
• By 15 years old 65% of children have seen online pornography. Children were most likely to see it via pop-ups than by searching for it.
• Just over half of boys (53%) who had seen pornography thought it was ‘realistic’.
• One in three parents (33%) claims to filter their child’s internet use and one in four (27%) uses monitoring software.
• Overall, only a quarter of children (27%) and a third of parents think parents are effective in helping to keep children safe online.
• The fourth page would give details of facebook and twitter pages, what support we provide (currently email based), as details of future features.
Should not have
• Images from the website...The brochure should be individual to the website as people will be requesting it from the website.
• Should not have the term Parental Control, but can use Parental Guidance

```html
<!DOCTYPE html>
<html lang="en">
<head>
<meta charset="utf-8">
<title>WebHaven Sentry – Internet Statistics</title>
<link rel="stylesheet" href="https://fonts.googleapis.com/css2?family=Open+Sans:wght@400;600&family=Zilla+Slab:wght@300;700&display=swap">
<style>
  :root {
    --ink: #1a1a1a;
    --sky: #29abe2;
    --navy: #003a57;
    --paper: #ffffff;
  }
  * { box-sizing: border-box; margin: 0; padding: 0; }
  html, body { width: 849px; height: 1200px; overflow: hidden; background: var(--paper); }
  .page { position: relative; width: 849px; height: 1200px; background: var(--paper); font-family: "Open Sans", Arial, sans-serif; color: var(--ink); }

  .stat { position: absolute; left: 118px; width: 612px; display: flex; align-items: center; gap: 14px; }
  .stat-icon { flex: 0 0 40px; width: 40px; height: 40px; }
  .stat-text { font-size: 18.5px; line-height: 25px; text-align: justify; }

  .rule { position: absolute; height: 7px; background: var(--sky); }
  .rule-top { left: 0; top: 463px; width: 788px; }
  .rule-bottom { left: 60px; top: 731px; width: 789px; }

  .title-band { position: absolute; left: 0; top: 482px; width: 849px; height: 238px; background: var(--navy); color: var(--paper); text-align: center; font-family: "Zilla Slab", Georgia, serif; padding-top: 52px; }
  .title-light { display: block; font-weight: 300; font-size: 55px; line-height: 62px; }
  .title-bold { display: block; font-weight: 700; font-size: 55px; line-height: 62px; }
</style>
</head>
<body>
<main class="page">

  <div class="stat" style="top:144px">
    <svg class="stat-icon" viewBox="0 0 40 40"><circle cx="20" cy="20" r="20" fill="var(--sky)"/><g fill="none" stroke="#fff" stroke-width="2"><circle cx="15" cy="15" r="4"/><circle cx="25" cy="15" r="4"/><path d="M8 28c0-5 3-8 7-8s7 3 7 8M18 28c0-5 3-8 7-8s7 3 7 8"/></g></svg>
    <p class="stat-text">1 in 3 Internet users are children.</p>
  </div>

  <div class="stat" style="top:197px">
    <svg class="stat-icon" viewBox="0 0 40 40"><circle cx="20" cy="20" r="20" fill="var(--sky)"/><g fill="none" stroke="#fff" stroke-width="2"><rect x="11" y="10" width="18" height="20" rx="1.5"/><circle cx="20" cy="17" r="3"/><path d="M14 26c1-4 3-5 6-5s5 1 6 5"/></g></svg>
    <p class="stat-text">1 in 5 eight to eleven-year olds have a social media profile.</p>
  </div>

  <div class="stat" style="top:248px">
    <svg class="stat-icon" viewBox="0 0 40 40"><circle cx="20" cy="20" r="20" fill="var(--sky)"/><g fill="none" stroke="#fff" stroke-width="2"><rect x="12" y="10" width="16" height="16" rx="3"/><path d="M16 18h2M22 18h2M16 23h8M14 30h12"/></g></svg>
    <p class="stat-text">1 in 3 children have been a victim of cyberbullying.</p>
  </div>

  <div class="stat" style="top:303px">
    <svg class="stat-icon" viewBox="0 0 40 40"><circle cx="20" cy="20" r="20" fill="var(--sky)"/><circle cx="20" cy="21" r="10" fill="none" stroke="#fff" stroke-width="2"/><text x="20" y="25" fill="#fff" font-family="Open Sans, sans-serif" font-size="10" font-weight="600" text-anchor="middle">18</text><path d="M28 8v6M25 11h6" stroke="#fff" stroke-width="2"/></svg>
    <p class="stat-text">By 15 years old 65% of children have seen online 3pornography. Children were most likely to see it via pop-ups than by searching for it.</p>
  </div>

  <div class="rule rule-top"></div>

  <header class="title-band">
    <h1><span class="title-light">The Internet Statistics</span><span class="title-bold">You Should to Know</span></h1>
  </header>

  <div class="rule rule-bottom"></div>

  <div class="stat" style="top:812px">
    <svg class="stat-icon" viewBox="0 0 40 40"><circle cx="20" cy="20" r="20" fill="var(--sky)"/><path d="M8 20c4-6 8-8 12-8s8 2 12 8c-4 6-8 8-12 8s-8-2-12-8z" fill="#fff"/><circle cx="20" cy="20" r="4" fill="var(--sky)"/></svg>
    <p class="stat-text">Just over half of boys (53%) who had seen pornography thought it was ‘realistic’.</p>
  </div>

  <div class="stat" style="top:894px">
    <svg class="stat-icon" viewBox="0 0 40 40"><circle cx="20" cy="20" r="20" fill="var(--sky)"/><g fill="none" stroke="#fff" stroke-width="2"><rect x="9" y="11" width="22" height="15" rx="1"/><path d="M16 30h8M20 26v4"/><circle cx="22" cy="18" r="3"/><path d="M24 20l3 3"/></g></svg>
    <p class="stat-text">One in three parents (33%) claims to filter their child’s internet use and one in four (27%) uses monitoring software.</p>
  </div>

  <div class="stat" style="top:971px">
    <svg class="stat-icon" viewBox="0 0 40 40"><circle cx="20" cy="20" r="20" fill="var(--sky)"/><path d="M20 9l10 4v7c0 6-4 10-10 12-6-2-10-6-10-12v-7z" fill="#fff"/><path d="M15 20l4 4 6-7" fill="none" stroke="var(--sky)" stroke-width="2.5"/></svg>
    <p class="stat-text">Overall, only a quarter of children (27%) and a third of parents think parents are effective in helping to keep children safe online.</p>
  </div>

</main>
</body>
</html>
```